Derek Folsom Resume

Need to update resume with latest position and ensure it stays to 2 pages, may need advice on what to get rid of and simply clean it up, already have a format that i like but am open to change but don't want to spend a fortune

```html
<!DOCTYPE html>
<html lang="en">
<head>
<meta charset="utf-8">
<title>Derek Folsom Resume</title>
<link href="https://fonts.googleapis.com/css2?family=Josefin+Sans:wght@300;400&display=swap" rel="stylesheet">
<style>
  :root {
    --ink: #111111;
    --paper: #ffffff;
    --sidebar: #000000;
    --sidebar-text: #ffffff;
    --body-text: #222222;
  }
  * { margin: 0; padding: 0; box-sizing: border-box; }
  html, body { width: 849px; height: 1200px; overflow: hidden; background: var(--paper); }
  body { font-family: "Josefin Sans", sans-serif; color: var(--body-text); }
  .resume { position: relative; width: 849px; height: 1200px; overflow: hidden; }

  .sidebar {
    position: absolute; left: 0; top: 0; width: 250px; height: 1200px;
    background: var(--sidebar); color: var(--sidebar-text);
  }
  .trait {
    position: absolute; left: 0; width: 250px; text-align: center;
    font-weight: 300; line-height: 1; text-transform: uppercase;
  }
  .trait--label { font-size: 25px; letter-spacing: 1.5px; }
  .trait--minor { font-size: 19px; letter-spacing: 1.2px; }
  .trait--large { font-size: 50px; letter-spacing: 2px; }
  .trait--medium { font-size: 34px; letter-spacing: 1.5px; text-transform: none; font-variant: small-caps; }
  .trait__sub { display: block; font-size: 15px; letter-spacing: 1px; margin-top: 1px; text-transform: uppercase; }

  .main { position: absolute; left: 280px; top: 0; width: 537px; }
  .name {
    position: absolute; left: 0; top: 30px; white-space: nowrap;
    font-size: 60px; font-weight: 300; font-variant: small-caps;
    letter-spacing: 3px; color: var(--ink); line-height: 1;
  }
  .contact {
    position: absolute; left: 0; top: 103px; white-space: nowrap;
    font-size: 17.5px; font-weight: 300; color: var(--ink);
  }

  .section { position: absolute; left: 0; width: 537px; }
  .section__title {
    font-size: 28px; font-weight: 300; font-variant: small-caps;
    letter-spacing: 1px; color: var(--ink); line-height: 1.1; margin-bottom: 4px;
  }
  .section p, .section li {
    font-size: 14px; font-weight: 300; font-variant: small-caps; line-height: 17px;
    text-align: justify; letter-spacing: 0.3px;
  }
  .section ul { list-style: none; }
  .gap { margin-top: 8px; }
  .role {
    font-size: 14px; font-weight: 300; font-variant: small-caps; text-decoration: underline;
    letter-spacing: 0.3px; margin-bottom: 8px; line-height: 17px;
  }
</style>
</head>
<body>
<div class="resume">
  <aside class="sidebar">
    <div class="trait trait--label" style="top:150px">knowledge</div>
    <div class="trait trait--large" style="top:306px">Loyal</div>
    <div class="trait trait--medium" style="top:447px">Aggressive<span class="trait__sub">energetic sales leader</span></div>
    <div class="trait trait--minor" style="top:582px">analytical skills</div>
    <div class="trait trait--minor" style="top:714px">consultative sales</div>
    <div class="trait trait--large" style="top:865px">Trust</div>
    <div class="trait trait--minor" style="top:998px">communication</div>
  </aside>

  <main class="main">
    <h1 class="name">Derek W. Folsom</h1>
    <div class="contact">555.010.4471 / derekfolsom@inboxly.com / 1187 Larkspur Court</div>

    <section class="section" style="top:180px">
      <h2 class="section__title">About me</h2>
      <p>Aggressive, loyal, energetic sales leader with a history of turning around underperforming teams, departments, and territories. Proven consultative sales approach with a focus on product knowledge, trust, and superior service. Strong interpersonal, communication, presentation, and analytical skills.</p>
      <ul>
        <li>- Developed effective sales incentives and initiatives that became company-wide best practices.</li>
        <li>- Drove revenue growth at direct, indirect, and retail sales levels; won multiple prestigious awards.</li>
        <li>- Recruited, developed, trained, and motivated high-energy sales/customer support teams.</li>
      </ul>
    </section>

    <section class="section" style="top:412px">
      <h2 class="section__title">core competencies include</h2>
      <p>New Business Development | C-Level Relationship Building | Complex Solution SellingHigh-Impact Sales Presentations | B2C &amp; B2B Channels | Machine to Machine Technology Channel Manager | Performance Management | Competitive Analysis | DealTrackrTerritory Sales Management | SaaS | Budgeting &amp; Forecasting | Vendor Management</p>
    </section>

    <section class="section" style="top:548px">
      <h2 class="section__title">Awards - Winning Sales Manager</h2>
      <p>Driving exceptional levels of sales results in competitive industries and changing environments.</p>
    </section>

    <section class="section" style="top:630px">
      <h2 class="section__title">Career Present</h2>
      <div class="role">Vantrell 2014 – Developmental Executive</div>
      <p>Sell wireless portfolio to the Office of Regional Defense, Office of Border Security, Office of Civic Justice, Hollis Grant Partners, and Aerovane.</p>
      <p class="gap">Increased overall revenue in assigned agencies 101.8% YOY.</p>
      <ul class="gap">
        <li>- Wireless Solutions: Facilitate critical communications for the national government through wireless solutions for networks, infrastructures, and security and surveillance.</li>
        <li>- Government Contracts: Navigate complex matrix of budgeting, bidding, and procurement for government contracts.</li>
        <li>- Collaboration: Work closely with solution engineers, project managers, and C-level executives on identifying the best solutions for their organizations.</li>
      </ul>
    </section>

    <section class="section" style="top:896px">
      <h2 class="section__title">Career History</h2>
      <div class="role">Northline Telecom 2014 - Client Business Manager</div>
      <p>Held national responsibility for sales of the entire Northline solutions portfolio to the Central Clearing Authority. Solutions included mobility, professional services, IP, Cloud, SaaS, Network infrastructure, and Managed Solutions.</p>
      <p class="gap">Sold nationwide managed Wi-Fi solution for all 12 Clearing Authority branch locations.</p>
      <ul class="gap">
        <li>- Complex Negotiations: Renewed three major contracts resulting in annual revenue of $12 million dollars.</li>
        <li>- Partner Relationships: Worked closely with system integrators, distributors, and value-added resellers.</li>
        <li>- Strategic Planning: Created strong nationwide strategic sales programs targeted to the Clearing Authority.</li>
      </ul>
    </section>
  </main>
</div>
</body>
</html>
```